Juniper Optometry Eye office bag

Looking for an eye catching design for our office. Fun, modern, bag that patients would love to use on daily.wish list : Eye Glasses vector Print of E chart"SEE THE DAY" is our office slogan

Target Market(s)

Modern patients

Industry/Entity Type

Optometrist

Font styles to use
Sans Serif

Colors
33a6d7
ffffff
fbee3d

Requirements
Must have
• Glasses, eyes, optical
Nice to have
• 3D design or something eye catching

```html
<!DOCTYPE html>
<html lang="en">
<head>
<meta charset="utf-8">
<title>Juniper Optometry – Office Bag</title>
<link rel="stylesheet" href="https://fonts.googleapis.com/css2?family=Oswald:wght@500;600&family=PT+Sans&family=Quicksand:wght@400;500&display=swap">
<style>
  :root {
    --stage: #939598;
    --paper: #ffffff;
    --ink: #231f20;
    --sunshine: #fdd533;
    --label: #1a1a1a;
    --pattern-light: #f2f2f2;
    --pattern-dark: #d4d4d4;
    --frame-dark: #1c1c1c;
    --frame-mid: #4a4a4a;
    --wordmark: #5f5f5f;
  }
  * { margin: 0; padding: 0; box-sizing: border-box; }
  html, body { width: 1200px; height: 493px; overflow: hidden; background: var(--stage); }
  .sheet { position: relative; width: 1200px; height: 493px; background: var(--stage); }

  .panel-label {
    position: absolute; top: 34px;
    font-family: "PT Sans", sans-serif; font-size: 19px; color: var(--label);
    text-align: center; transform: translateX(-50%); white-space: nowrap;
  }

  .panel { position: absolute; top: 72px; height: 381px; background: var(--paper); overflow: hidden; }
  .panel--side { width: 125px; }
  .panel--face { width: 386px; }
  .panel--left { left: 40px; }
  .panel--front { left: 198px; }
  .panel--right { left: 616px; }
  .panel--back { left: 774px; }

  .glasses-pattern {
    position: absolute; inset: 0;
    background: linear-gradient(180deg, var(--pattern-light), var(--pattern-dark));
  }
  .contact-column {
    position: absolute; left: 22px; right: 22px; top: 206px; bottom: 8px;
    background: var(--paper);
  }
  .contact {
    position: absolute; left: 0; right: 0; text-align: center;
    font-family: "Quicksand", sans-serif; font-size: 5.6px; line-height: 7.6px; color: var(--ink);
  }
  .contact-icon { display: block; width: 10px; height: 10px; margin: 0 auto 3px; }
  .contact--web { top: 4px; }
  .contact--addr-one { top: 37px; }
  .contact--phone-one { top: 70px; }
  .contact--addr-two { top: 103px; }
  .contact--phone-two { top: 136px; }

  .frames-art {
    position: absolute; left: 109px; top: 90px; width: 166px; height: 61px;
    background: radial-gradient(ellipse at 50% 40%, var(--frame-mid), var(--frame-dark));
    border-radius: 10px 10px 40px 40px;
  }
  .slogan { position: absolute; left: 110px; top: 254px; display: flex; align-items: flex-end; }
  .slogan-see {
    font-family: "Oswald", sans-serif; font-weight: 600; font-size: 118px; line-height: 84px;
    color: var(--sunshine); letter-spacing: -2px; transform: scaleX(0.92); transform-origin: left bottom;
    margin-right: -8px;
  }
  .slogan-rest {
    font-family: "Oswald", sans-serif; font-weight: 600; font-size: 30px; line-height: 37px;
    color: var(--ink); letter-spacing: -0.5px; margin-bottom: -7px;
  }

  .brand { position: absolute; left: 0; right: 0; top: 118px; text-align: center; }
  .brand-mark { width: 82px; height: 82px; margin: 0 auto 12px; background: var(--sunshine); }
  .brand-name {
    font-family: "Quicksand", sans-serif; font-weight: 400; font-size: 17px; line-height: 20px;
    letter-spacing: 1.5px; color: var(--wordmark); text-transform: uppercase;
  }
</style>
</head>
<body>
<main class="sheet">
  <p class="panel-label" style="left:102px">Left Side</p>
  <p class="panel-label" style="left:391px">Front</p>
  <p class="panel-label" style="left:679px">Right Side</p>
  <p class="panel-label" style="left:967px">Back</p>

  <section class="panel panel--side panel--left">
    <div class="glasses-pattern" role="img" aria-label="Repeating pattern of small black eyeglass frames"></div>
    <div class="contact-column">
      <p class="contact contact--web">
        <svg class="contact-icon" viewBox="0 0 10 10"><rect width="10" height="10" fill="var(--sunshine)"/><circle cx="5" cy="5" r="3" fill="none" stroke="#fff" stroke-width="0.8"/><path d="M2 5h6M5 2c-1.5 2-1.5 4 0 6M5 2c1.5 2 1.5 4 0 6" fill="none" stroke="#fff" stroke-width="0.6"/></svg>
        www.junipersee.com
      </p>
      <p class="contact contact--addr-one">
        <svg class="contact-icon" viewBox="0 0 10 10"><rect width="10" height="10" fill="var(--sunshine)"/><path d="M5 8.5C3 6 2.8 5 2.8 4.2a2.2 2.2 0 0 1 4.4 0C7.2 5 7 6 5 8.5z" fill="#fff"/><circle cx="5" cy="4.2" r="0.8" fill="var(--sunshine)"/></svg>
        4820 Alder Grove Ave.<br>Fairview, CA 90210
      </p>
      <p class="contact contact--phone-one">
        <svg class="contact-icon" viewBox="0 0 10 10"><rect width="10" height="10" fill="var(--sunshine)"/><path d="M3 2.2l1.2 1.6-.7.8c.4.9 1 1.5 1.9 1.9l.8-.7 1.6 1.2-.8 1c-2.6-.3-4.5-2.2-4.8-4.8z" fill="#fff"/></svg>
        (555) 014 - 2010
      </p>
      <p class="contact contact--addr-two">
        <svg class="contact-icon" viewBox="0 0 10 10"><rect width="10" height="10" fill="var(--sunshine)"/><path d="M5 8.5C3 6 2.8 5 2.8 4.2a2.2 2.2 0 0 1 4.4 0C7.2 5 7 6 5 8.5z" fill="#fff"/><circle cx="5" cy="4.2" r="0.8" fill="var(--sunshine)"/></svg>
        2290 Maple Crest St# 4<br>Linden Hills, CA 90211
      </p>
      <p class="contact contact--phone-two">
        <svg class="contact-icon" viewBox="0 0 10 10"><rect width="10" height="10" fill="var(--sunshine)"/><path d="M3 2.2l1.2 1.6-.7.8c.4.9 1 1.5 1.9 1.9l.8-.7 1.6 1.2-.8 1c-2.6-.3-4.5-2.2-4.8-4.8z" fill="#fff"/></svg>
        (555) 019 - 4020
      </p>
    </div>
  </section>

  <section class="panel panel--face panel--front">
    <div class="frames-art" role="img" aria-label="Large black eyeglass frames illustration"></div>
    <h1 class="slogan">
      <span class="slogan-see">SEE</span>
      <span class="slogan-rest">THE<br>DAY</span>
    </h1>
  </section>

  <section class="panel panel--side panel--right">
    <div class="glasses-pattern" role="img" aria-label="Repeating pattern of small black eyeglass frames"></div>
    <div class="contact-column">
      <p class="contact contact--web">
        <svg class="contact-icon" viewBox="0 0 10 10"><rect width="10" height="10" fill="var(--sunshine)"/><circle cx="5" cy="5" r="3" fill="none" stroke="#fff" stroke-width="0.8"/><path d="M2 5h6M5 2c-1.5 2-1.5 4 0 6M5 2c1.5 2 1.5 4 0 6" fill="none" stroke="#fff" stroke-width="0.6"/></svg>
        www.junipersee.com
      </p>
      <p class="contact contact--addr-one">
        <svg class="contact-icon" viewBox="0 0 10 10"><rect width="10" height="10" fill="var(--sunshine)"/><path d="M5 8.5C3 6 2.8 5 2.8 4.2a2.2 2.2 0 0 1 4.4 0C7.2 5 7 6 5 8.5z" fill="#fff"/><circle cx="5" cy="4.2" r="0.8" fill="var(--sunshine)"/></svg>
        4820 Alder Grove Ave.<br>Fairview, CA 90210
      </p>
      <p class="contact contact--phone-one">
        <svg class="contact-icon" viewBox="0 0 10 10"><rect width="10" height="10" fill="var(--sunshine)"/><path d="M3 2.2l1.2 1.6-.7.8c.4.9 1 1.5 1.9 1.9l.8-.7 1.6 1.2-.8 1c-2.6-.3-4.5-2.2-4.8-4.8z" fill="#fff"/></svg>
        (555) 014 - 2010
      </p>
      <p class="contact contact--addr-two">
        <svg class="contact-icon" viewBox="0 0 10 10"><rect width="10" height="10" fill="var(--sunshine)"/><path d="M5 8.5C3 6 2.8 5 2.8 4.2a2.2 2.2 0 0 1 4.4 0C7.2 5 7 6 5 8.5z" fill="#fff"/><circle cx="5" cy="4.2" r="0.8" fill="var(--sunshine)"/></svg>
        2290 Maple Crest St# 4<br>Linden Hills, CA 90211
      </p>
      <p class="contact contact--phone-two">
        <svg class="contact-icon" viewBox="0 0 10 10"><rect width="10" height="10" fill="var(--sunshine)"/><path d="M3 2.2l1.2 1.6-.7.8c.4.9 1 1.5 1.9 1.9l.8-.7 1.6 1.2-.8 1c-2.6-.3-4.5-2.2-4.8-4.8z" fill="#fff"/></svg>
        (555) 019 - 4020
      </p>
    </div>
  </section>

  <section class="panel panel--face panel--back">
    <div class="brand">
      <div class="brand-mark"></div>
      <p class="brand-name">Juniper Optometry</p>
    </div>
  </section>
</main>
</body>
</html>
```